Postcard for Construction Industry

www.brightmarktallies.com is our website.

We offer services to construction companies to read blueprints and give them a materials quantity list of how much work they need to do on a project. We service all types of companies such as painting, flooring, siding, drywall, Acoustical ceiling tile, framing, millwork, and much more.

I want a postcard designed that can be sent via email AND regular mail to introduce our company.

I've also attached another document with more detailed explanation, pricing, etc.

Important:
The postcard must appeal to the construction industry so they pick it up and read it.

Target Market(s)

Construction Industry

Industry/Entity Type

Construction

Font styles to use
Serif

Requirements
Must have
• Call to Action -
• Register on our site
• Get a FREE Quote
• Trades Serviced should be referenced on front so the person reading it immediately knows 2 things. Free Construction Takeoffs. List of Trades.
Nice to have
• Construction Images
• It's so EASY!!!
• -You load your plans
• -We give you a quote
• -If you approve, we do the work!
• NO OBLIGATION TO PURCHASE
Should not have
• Pricing - other than FREE Quotes
• Should not have phone number Prominent. It can be small on the back. (I want them to register via website)

```html
<!DOCTYPE html>
<html lang="en">
<head>
<meta charset="utf-8">
<title>Brightmark Tallies Postcard</title>
<link href="https://fonts.googleapis.com/css2?family=Roboto:wght@400;500;700;900&family=Roboto+Condensed:wght@700&display=swap" rel="stylesheet">
<style>
  :root{
    --stage:#2b2b2d;
    --navy:#0e2548;
    --navy-deep:#0a1b36;
    --blue:#1d63b3;
    --sky:#3d93e0;
    --light-blue:#5fb2f0;
    --white:#ffffff;
    --line:#b9bec6;
  }
  *{box-sizing:border-box;margin:0;padding:0}
  html,body{width:804px;height:1200px;overflow:hidden;background:var(--stage);font-family:"Roboto",Arial,sans-serif}
  .card{position:absolute;left:29px;width:746px;height:564px;overflow:hidden;background:var(--white)}
  .front{top:20px}
  .back{top:611px}
  .abs{position:absolute}

  /* front */
  .site-photo{left:0;top:0;width:746px;height:564px;
    background:linear-gradient(180deg,#eef3f8 0%,#d5e3ef 40%,#a9bccb 60%,#8a8f86 76%,#3a3f44 100%)}
  .foreground-photo{left:0;top:350px;width:437px;height:150px;
    background:linear-gradient(90deg,rgba(120,140,160,.35) 0%,rgba(205,170,80,.45) 55%,rgba(120,130,140,.3) 100%)}
  .bottom-shade{left:0;top:430px;width:437px;height:134px;background:linear-gradient(180deg,rgba(10,27,54,0) 0%,rgba(10,27,54,.85) 60%)}
  .brand{left:28px;top:24px;display:flex;align-items:center;gap:10px}
  .brand-mark{width:16px;height:16px;background:var(--blue)}
  .brand-name{font-weight:900;font-size:23px;letter-spacing:.5px;color:var(--navy)}
  .brand-tag{font-size:11px;line-height:12px;color:var(--blue)}
  .headline{left:28px;top:98px;font-weight:900;font-size:25px;line-height:29px;color:var(--blue)}
  .easy{left:28px;top:170px;color:var(--navy);font-size:20px;line-height:25px;font-weight:500}
  .easy strong{font-size:23px;font-weight:700;display:block;margin-bottom:2px}
  .no-obligation{left:28px;top:318px;font-weight:700;font-size:17px;color:var(--light-blue);letter-spacing:.3px}
  .tagline{left:28px;top:492px;font-weight:700;font-size:19px;line-height:23px;color:var(--white)}

  .trades-panel{left:437px;top:0;width:309px;height:564px;background:linear-gradient(180deg,var(--navy) 0%,var(--navy-deep) 100%)}
  .work-photo{border:3px solid var(--white)}
  .work-photo.one{left:468px;top:28px;width:255px;height:98px;background:linear-gradient(135deg,#8fb7d9,#b8574a 60%,#5c4a3c)}
  .work-photo.two{left:482px;top:134px;width:250px;height:96px;background:linear-gradient(135deg,#a9c6dd,#6c7e8c 55%,#c9a548)}
  .trades-bar{left:437px;top:240px;width:309px;height:34px;background:var(--sky);color:var(--white);
    font-family:"Roboto Condensed",Arial,sans-serif;font-size:19px;padding:6px 0 0 24px;letter-spacing:.5px}
  .trades-intro{left:461px;top:284px;width:270px;font-size:13.5px;line-height:17px;color:var(--white)}
  .trade-list{top:348px;list-style:none;color:var(--white);font-size:15px;line-height:21px}
  .trade-list li::before{content:"• "}
  .trade-list.col-a{left:461px;width:130px}
  .trade-list.col-b{left:601px;width:130px}
  .register{left:461px;top:498px;font-size:14px;color:var(--white)}
  .website{left:461px;top:518px;font-size:15px;font-weight:700;color:var(--light-blue)}

  /* back */
  .question-panel{left:0;top:0;width:360px;height:564px;
    background:linear-gradient(180deg,#132f5c 0%,#1a4277 45%,#0d2547 100%)}
  .back .brand{left:38px;top:22px}
  .back .brand-name{color:var(--white);font-size:21px}
  .question{left:72px;width:236px;height:80px;background:var(--white);border-radius:2px;
    display:flex;align-items:center;justify-content:center;text-align:center;
    font-weight:700;font-size:16px;line-height:20px;color:var(--navy);padding:0 12px}
  .q1{top:74px}.q2{top:192px}.q3{top:310px}
  .tick{left:26px;width:36px;height:36px}
  .t1{top:96px}.t2{top:214px}.t3{top:332px}
  .discount{left:0;top:410px;width:360px;text-align:center;color:var(--white);font-size:15.5px}
  .turnaround{left:0;top:434px;width:360px;height:28px;background:var(--sky);color:var(--white);
    text-align:center;font-weight:700;font-size:16px;line-height:28px}
  .contact{left:0;top:472px;width:360px;text-align:center;color:var(--white);font-size:13.5px;line-height:17px}
  .stamp{left:636px;top:22px;width:88px;height:104px;border:1.5px solid var(--line)}
  .address-line{left:398px;width:326px;height:1.5px;background:var(--line)}
  .l1{top:390px}.l2{top:446px}.l3{top:494px}
</style>
</head>
<body>

<section class="card front">
  <div class="abs site-photo" role="img" aria-label="Construction site with cranes and building frame under a pale sky"></div>
  <div class="abs foreground-photo" role="img" aria-label="Photo of a hard hat resting on rolled blueprints and a tablet"></div>
  <div class="abs bottom-shade"></div>

  <div class="abs brand">
    <span class="brand-mark"></span>
    <span class="brand-name">BRIGHTMARK TALLIES</span>
  </div>
  <div class="abs brand-tag" style="left:54px;top:52px">Commercial Construction Professionals</div>

  <h1 class="abs headline">COMMERCIAL CONSTRUCTION<br>TAKEOFF SERVICES</h1>
  <p class="abs easy"><strong>It's so EASY!!!</strong>You load your plans,<br>We give you a quote<br>If you approve,<br>we do the work!</p>
  <p class="abs no-obligation">NO OBLIGATION TO PURCHASE</p>
  <p class="abs tagline">Affordable, Professional,<br>Commercial Blueprint Quantity Takeoffs</p>

  <div class="abs trades-panel"></div>
  <div class="abs work-photo one" role="img" aria-label="Photo of a roofer installing shingles"></div>
  <div class="abs work-photo two" role="img" aria-label="Photo of a worker measuring on a job site"></div>
  <div class="abs trades-bar">TRADES SERVICED</div>
  <p class="abs trades-intro">Our experts will assist you with commercial quantity takeoffs for most construction trades including:</p>
  <ul class="abs trade-list col-a">
    <li>Floor &amp;<br>&nbsp;&nbsp;Wallcoverings</li>
    <li>Painting</li>
    <li>Sheetrock</li>
  </ul>
  <ul class="abs trade-list col-b">
    <li>Roofing</li>
    <li>Siding</li>
    <li>Foundations &amp;<br>&nbsp;&nbsp;Paving</li>
  </ul>
  <p class="abs register">Register you project today</p>
  <p class="abs website">www.brightmarktallies.com</p>
</section>

<section class="card back">
  <div class="abs question-panel" role="img" aria-label="Blue-tinted blueprints and drafting tools"></div>

  <div class="abs brand">
    <span class="brand-mark" style="background:var(--white)"></span>
    <span class="brand-name">BRIGHTMARK TALLIES</span>
  </div>
  <div class="abs brand-tag" style="left:64px;top:48px;color:var(--white)">Commercial Construction Professionals</div>

  <svg class="abs tick t1" viewBox="0 0 36 36"><path d="M5 18 L14 28 L31 7" fill="none" stroke="#5fb2f0" stroke-width="5" stroke-linecap="round" stroke-linejoin="round"/></svg>
  <svg class="abs tick t2" viewBox="0 0 36 36"><path d="M5 18 L14 28 L31 7" fill="none" stroke="#5fb2f0" stroke-width="5" stroke-linecap="round" stroke-linejoin="round"/></svg>
  <svg class="abs tick t3" viewBox="0 0 36 36"><path d="M5 18 L14 28 L31 7" fill="none" stroke="#5fb2f0" stroke-width="5" stroke-linecap="round" stroke-linejoin="round"/></svg>

  <div class="abs question q1">Can't find the time<br>to bid new projects?</div>
  <div class="abs question q2">Can't find the budget<br>for a full-time<br>expert?</div>
  <div class="abs question q3">Do you want to verify<br>the quantities from<br>your subs?</div>

  <p class="abs discount">High-Volume Pricing Discounts Available</p>
  <p class="abs turnaround">Turnaround in as low as 24 hours!!</p>
  <p class="abs contact">Contact Us<br>Dale Merrin, Owner<br>555-014-2290<br>dale@brightmarktallies.com</p>

  <div class="abs stamp"></div>
  <div class="abs address-line l1"></div>
  <div class="abs address-line l2"></div>
  <div class="abs address-line l3"></div>
</section>

</body>
</html>
```